Junior Showdown Flyer for Holiday Program

Need a one page flyer, can be back to front or one page, ensuring you can fit all information, colourful, aimed at a market of 8-13 year old boys and girls.
The flyer needs to be noticed, needs to have certain information on it and needs to be Autralian Rule Football orientated.
Have uploaded file so you can understand the style (not content), style of flyer I am looking at getting submitted.

Target Market(s)

8-13 year old boys and girls and their parents.

Requirements
Must have
• Junior Showdown Event
• Price for Junior Showdown Day will be $85
• Strictly Limited Places, only the best footballers should enter this challenge
• Inaugural event, be the first Junior Showdown Winner for your age!
• Do you love a challenge! Put yourself to the test!
• Are you up to it - Water Slide Goal Kicking Contest! The fastest kick in the West (tested by our very own speed gun)! Can you survive the Football Gladiator Course or Topple Mania Goal Kicking! These challenges are crazy are super fun!
• If you think you can deliver on the big stage then this is for YOU!
• All District age winners will receive prizes, awards and the adulation from all their peers!
• Year's 3-5 from 9am to 12pm
• Year's 6-8 from 1-4pm
• All challengers compete against their own age
• Lunch Provided
• Monday 16th April - Kestrel Bay Junior Showdown Day at Brindle Park
• Tuesday 17th April - Marlow Ridge Junior Showdown Day at Collumbi Reserve
• Wednesday 18th April - Tarrin Junior Showdown Day - Yandell Football Club
• Every Challenge Participant receives a District Football!
• Need to put all 3 District Football Logos on the bottom of the flyer, logos attached at bottom.
Nice to have
• Plenty of colour, if you can fit all information on one page that would be fine
Should not have
• Dull, boring, any footballs should be Aussie Rules footballs not NFL or soccer

```html
<!DOCTYPE html>
<html lang="en">
<head>
<meta charset="utf-8">
<title>Junior Showdown Event Flyer</title>
<link href="https://fonts.googleapis.com/css2?family=Arimo:wght@400;700&family=Exo+2:ital,wght@1,900&display=swap" rel="stylesheet">
<style>
  :root {
    --green: #6a9e2e;
    --red: #d9161c;
    --sky: #1f9ad6;
    --panel: #239ed8;
    --ink: #1a1a1a;
    --white: #ffffff;
    --backdrop: #e9e4dc;
    --navy: #1d3f8a;
    --teal: #178a7a;
    --crimson: #c8202a;
  }
  * { box-sizing: border-box; margin: 0; padding: 0; }
  html, body { width: 1200px; height: 1200px; overflow: hidden; }
  body { background: var(--backdrop); font-family: "Arimo", Arial, sans-serif; position: relative; }

  .flyer {
    position: absolute; left: 193px; top: 30px;
    width: 984px; height: 1378px;
    transform: scale(0.827); transform-origin: 0 0;
    background: var(--white); overflow: hidden;
    box-shadow: 0 6px 18px rgba(0,0,0,.25);
  }
  .stadium-scene {
    position: absolute; left: 0; top: 200px; width: 984px; height: 1178px;
    background: linear-gradient(180deg, #ffffff 0%, #ffffff 12%, #eaf2f8 38%, #d3e2ea 66%, #b9d0d8 76%, #7bb153 84%, #4a8a2f 100%);
  }
  .header-bands { position: absolute; left: 0; top: 0; width: 984px; height: 240px; }
  .event-title {
    position: absolute; left: 0; top: 58px; width: 984px; text-align: center;
    font-family: "Exo 2", Arial, sans-serif; font-style: italic; font-weight: 900;
    font-size: 74px; letter-spacing: -1px; color: var(--white); text-transform: uppercase;
  }

  .side-panel {
    position: absolute; left: 30px; top: 375px; width: 322px; height: 1003px;
    background: var(--panel);
  }
  .photo-circle {
    position: absolute; border-radius: 50%; border: 5px solid var(--white);
  }
  .photo-top {
    left: 32px; top: 230px; width: 320px; height: 320px;
    background: radial-gradient(circle at 50% 45%, #c36a4a 0%, #7a5a3e 40%, #4f5e3a 75%, #3a4430 100%);
  }
  .photo-bottom {
    left: 49px; top: 1050px; width: 290px; height: 290px;
    background: radial-gradient(circle at 50% 45%, #5b4a6a 0%, #38405a 45%, #2f6a35 85%, #2a5a2c 100%);
  }
  .price-block {
    position: absolute; left: 30px; top: 575px; width: 322px; text-align: center; color: var(--white);
  }
  .price-label { font-size: 27px; line-height: 35px; }
  .price-value { font-size: 44px; margin-top: 10px; }
  .price-rule { width: 180px; height: 3px; background: var(--white); margin: 18px auto 0; }
  .panel-copy {
    position: absolute; left: 46px; top: 768px; width: 306px;
    color: var(--white); font-size: 18px; line-height: 24px; text-align: justify;
  }
  .panel-copy p { margin-bottom: 4px; }

  .details {
    position: absolute; left: 374px; top: 284px; width: 580px; list-style: none;
    color: var(--ink); font-size: 18.5px; line-height: 23px;
  }
  .details li { position: relative; padding-left: 20px; margin-bottom: 15px; }
  .details li::before {
    content: ""; position: absolute; left: 0; top: 8px;
    width: 7px; height: 7px; border-radius: 50%; background: var(--red);
  }
  .details strong { font-weight: 700; }

  .district-row {
    position: absolute; left: 384px; top: 920px; width: 580px; display: flex; justify-content: space-between;
  }
  .district-mark { display: flex; align-items: center; gap: 10px; font-weight: 700; font-size: 20px; }
  .district-mark .dot { width: 34px; height: 34px; border-radius: 50%; }
  .mark-gulls { color: var(--navy); }
  .mark-gulls .dot { background: var(--navy); }
  .mark-tarrin { color: var(--teal); }
  .mark-tarrin .dot { background: var(--teal); }
  .mark-hounds { color: var(--crimson); }
  .mark-hounds .dot { background: var(--crimson); }
</style>
</head>
<body>
  <main class="flyer">
    <div class="stadium-scene" role="img" aria-label="Football stadium with tall white goal posts and a red Australian Rules football resting on green grass"></div>

    <svg class="header-bands" viewBox="0 0 984 240" aria-hidden="true">
      <polygon points="0,0 984,0 984,145 0,185" fill="var(--green)"/>
      <polygon points="0,185 984,145 984,155 480,195 0,235" fill="var(--red)"/>
      <polygon points="480,195 984,155 984,223" fill="var(--sky)"/>
    </svg>
    <h1 class="event-title">Junior Showdown Event</h1>

    <aside class="side-panel"></aside>
    <div class="photo-circle photo-top" role="img" aria-label="Junior footballers leaping for a high mark"></div>

    <div class="price-block">
      <p class="price-label">Price for Junior Showdown<br>Day will be</p>
      <p class="price-value">$85</p>
      <div class="price-rule"></div>
    </div>

    <div class="panel-copy">
      <p>Do you love a challenge! Put yourself to the test!</p>
      <p>Are you up to it - Water Slide Goal Kicking Contest!</p>
      <p>The fastest kick in the West (tested by our very own speed gun)!</p>
      <p>Can you survive the Football Gladiator Course or Topple Mania Goal Kicking! These challenges are crazy are super fun!</p>
    </div>

    <div class="photo-circle photo-bottom" role="img" aria-label="Senior footballers contesting the ball in a match"></div>

    <ul class="details">
      <li>Strictly Limited Places, only the best footballers should enter this challenge</li>
      <li>Inaugural event, be the first Junior Showdown Winner for your age!</li>
      <li>If you think you can deliver on the big stage then this is for YOU!</li>
      <li>All District age winners will receive prizes, awards and the adulation from all their peers!</li>
      <li><strong>Year's 3-5 from 9am to 12pm</strong></li>
      <li><strong>Year's 6-8 from 1-4pm</strong></li>
      <li>All challengers compete against their own age</li>
      <li>Lunch Provided</li>
      <li>Monday 16th April - Kestrel Bay Junior Showdown Day at Brindle Park</li>
      <li><strong>Tuesday 17th April</strong> - Marlow Ridge Junior Showdown Day at Collumbi Reserve</li>
      <li><strong>Wednesday 18th April</strong> - Tarrin Junior Showdown Day - Yandell Football Club</li>
      <li>Every Challenge Participant receives a District Football!</li>
    </ul>

    <div class="district-row">
      <div class="district-mark mark-gulls"><span>Gulls District</span><span class="dot"></span></div>
      <div class="district-mark mark-tarrin"><span>Tarrin District</span><span class="dot"></span></div>
      <div class="district-mark mark-hounds"><span>Hounds District</span><span class="dot"></span></div>
    </div>
  </main>
</body>
</html>
```